Business card design Needed for new logo / Construction business, home extensions and new builds

We need a business card design using our new logo files which i will attach to this project :)

We are a small construction business specialising in home extensions, new builds and property development. We are very ambitious and would appreciate professional and elegant designs for our new business card.

Very serious about using the services on Sketchwharf and recently acquired our new logo from here :)

Please get involved, i will feedback when i can as i am very busy but can respond daily, thanks

Target Market(s)

People that want to build onto their houses, new building developments or adding too their existing property

Industry/Entity Type

Construction

Contact Information for Business Card

Thornley Pike Construction, Wilbur Fenwick (Managing Director), Tel 07829456172, email - info@thornley-pike, www.thornley-pike.co.uk

Colors

Designer to choose colors to be used in the design.

Requirements
Must have
• I like a deep grey on the back please. A lot of you have provided black from and back, try mixing things up a little. The black looks cool 😎 Thanks

```html
<!DOCTYPE html>
<html lang="en">
<head>
<meta charset="utf-8">
<title>Thornley Pike Construction – Business Card</title>
<link rel="stylesheet" href="https://fonts.googleapis.com/css2?family=Cinzel:wght@600&family=Arimo:wght@400&display=swap">
<style>
  :root {
    --backdrop: #3a3a3a;
    --card-back: #2f2f2f;
    --card-back-text: #d9d9d9;
    --card-front: #ffffff;
    --gold: #c8961e;
    --gold-light: #f1cf6e;
    --silver: #b9bcbf;
    --ink: #3c3c3c;
    --rule: #cfcfcf;
  }
  * { margin: 0; padding: 0; box-sizing: border-box; }
  html, body { width: 1200px; height: 689px; overflow: hidden; }
  body {
    background: var(--backdrop);
    position: relative;
    font-family: "Arimo", Arial, sans-serif;
  }
  .card {
    position: absolute;
    top: 195px;
    width: 525px;
    height: 300px;
    border-radius: 18px;
    overflow: hidden;
  }
  /* Back side */
  .card-back {
    left: 45px;
    background: var(--card-back);
  }
  .card-back .brand-name {
    position: absolute;
    left: 0; right: 0; top: 105px;
    text-align: center;
    font-family: "Cinzel", Georgia, serif;
    font-weight: 600;
    font-size: 26px;
    letter-spacing: 2px;
    color: #3d3d3d;
  }
  .card-back .website {
    position: absolute;
    left: 0; right: 0; bottom: 38px;
    text-align: center;
    font-size: 13px;
    color: var(--card-back-text);
    letter-spacing: 0.3px;
  }
  /* Front side */
  .card-front {
    left: 630px;
    background: var(--card-front);
  }
  .brand-block {
    position: absolute;
    left: 22px; top: 110px;
    width: 215px;
    text-align: center;
  }
  .brand-mark {
    display: block;
    width: 14px; height: 14px;
    margin: 0 auto 10px;
    background: var(--gold);
  }
  .brand-block .brand-name {
    font-family: "Cinzel", Georgia, serif;
    font-weight: 600;
    font-size: 17px;
    line-height: 1.25;
    letter-spacing: 1px;
    color: var(--gold);
  }
  .divider {
    position: absolute;
    left: 255px; top: 60px;
    width: 1px; height: 140px;
    background: var(--rule);
  }
  .details {
    position: absolute;
    left: 282px; top: 70px;
  }
  .person-name {
    font-family: "Cinzel", Georgia, serif;
    font-weight: 600;
    font-size: 19px;
    color: var(--gold);
    letter-spacing: 0.5px;
  }
  .person-title {
    font-size: 12px;
    color: var(--ink);
    margin-top: 2px;
  }
  .contact-list {
    list-style: none;
    margin-top: 26px;
  }
  .contact-list li {
    display: flex;
    align-items: center;
    gap: 8px;
    font-size: 13px;
    color: var(--ink);
    margin-bottom: 5px;
  }
  .contact-list svg { width: 11px; height: 11px; fill: var(--gold); flex: none; }
  .edge-band {
    position: absolute;
    left: 0; right: 0; bottom: 0;
    height: 9px;
    display: flex;
  }
  .edge-band .gold-part { flex: 0 0 70%; background: linear-gradient(90deg, var(--gold), var(--gold-light)); }
  .edge-band .silver-part { flex: 1; background: linear-gradient(90deg, #dadcde, var(--silver)); }
</style>
</head>
<body>

<section class="card card-back" aria-label="Card back">
  <div class="brand-name">Thornley Pike</div>
  <div class="website">www.thornley-pike.co.uk</div>
</section>

<section class="card card-front" aria-label="Card front">
  <div class="brand-block">
    <span class="brand-mark"></span>
    <div class="brand-name">Thornley Pike<br>Construction</div>
  </div>

  <div class="divider"></div>

  <div class="details">
    <div class="person-name">WILBUR FENWICK</div>
    <div class="person-title">Managing Director</div>
    <ul class="contact-list">
      <li>
        <svg viewBox="0 0 24 24"><path d="M6.6 10.8a15 15 0 0 0 6.6 6.6l2.2-2.2c.3-.3.7-.4 1-.2 1.1.4 2.3.6 3.6.6.6 0 1 .4 1 1V20c0 .6-.4 1-1 1C10.6 21 3 13.4 3 4c0-.6.4-1 1-1h3.5c.6 0 1 .4 1 1 0 1.3.2 2.5.6 3.6.1.3 0 .7-.2 1z"/></svg>
        07829456172
      </li>
      <li>
        <svg viewBox="0 0 24 24"><path d="M2 5h20v14H2zM4 7v.5l8 5 8-5V7z"/></svg>
        info@thornley-pike
      </li>
      <li>
        <svg viewBox="0 0 24 24"><circle cx="12" cy="12" r="10"/></svg>
        www.thornley-pike.co.uk
      </li>
    </ul>
  </div>

  <div class="edge-band"><span class="gold-part"></span><span class="silver-part"></span></div>
</section>

</body>
</html>
```